Private Investigation Business Card Design

I need a business card for a new private investigation company named Kestrel Inquiries. I perform mainly surveillance jobs, vehicle repossessions, document serves etc. The final design should aim for a professional look. The logo has a magnifying glass with stick man arms and legs and is in a running action to show the "Kestrel" aspect of the name. If the colour scheme could remain the same as the website www.kestrelinquiries-example.com.au with silvers,blacks and a couple electric blue highlights.
Business
Contact Information for Business Card
Morgan Pellwick
Kestrel Inquiries
0487362914
PO Box 58, Ferndale NSW 2317
info@kestrelinquiries-example.com.au
www.kestrelinquiries-example.com.au

```html
<!DOCTYPE html>
<html lang="en">
<head>
<meta charset="utf-8">
<title>Kestrel Inquiries – Business Card</title>
<link rel="stylesheet" href="https://fonts.googleapis.com/css2?family=Arimo:wght@400;700&display=swap">
<style>
  :root {
    --bg: #2a2a2c;
    --silver-light: #d6d6d8;
    --silver-mid: #a9a9ad;
    --silver-dark: #7e7e83;
    --ink: #1b1b1d;
    --ink-soft: #55565a;
    --paper: #ffffff;
    --paper-shade: #ececee;
  }
  * { box-sizing: border-box; margin: 0; padding: 0; }
  html, body { width: 1200px; height: 871px; overflow: hidden; }
  body {
    background: var(--bg);
    font-family: "Arimo", Arial, sans-serif;
    display: flex;
    flex-direction: column;
    align-items: center;
    justify-content: center;
    gap: 40px;
  }
  .card {
    width: 640px;
    height: 366px;
    position: relative;
    overflow: hidden;
    box-shadow: 0 10px 30px rgba(0,0,0,.45);
  }

  /* Back side */
  .card-back {
    background: linear-gradient(160deg, var(--silver-light) 0%, var(--silver-mid) 55%, var(--silver-dark) 100%);
  }
  .card-back .brand {
    position: absolute;
    left: 120px;
    top: 130px;
    display: flex;
    align-items: center;
    gap: 14px;
    font-size: 44px;
    font-weight: 700;
    color: var(--ink-soft);
    letter-spacing: 1px;
  }
  .brand .dot {
    width: 22px; height: 22px; border-radius: 50%;
    background: currentColor;
  }
  .card-back .web {
    position: absolute;
    left: 120px;
    top: 214px;
    display: flex;
    align-items: center;
    gap: 10px;
    font-size: 15px;
    letter-spacing: 2px;
    color: var(--ink-soft);
  }
  .card-back .web .rule {
    width: 60px; height: 1px; background: var(--ink-soft);
  }

  /* Front side */
  .card-front {
    background: linear-gradient(170deg, var(--paper) 0%, var(--paper) 60%, var(--paper-shade) 100%);
  }
  .card-front .side-band {
    position: absolute;
    left: 0; top: 0; bottom: 0;
    width: 58px;
    background: linear-gradient(90deg, var(--silver-light), var(--silver-dark));
    border-right: 6px solid var(--ink);
    box-shadow: 3px 0 0 var(--paper), 5px 0 0 var(--silver-mid);
  }
  .card-front .brand {
    position: absolute;
    right: 58px;
    top: 48px;
    display: flex;
    align-items: center;
    gap: 12px;
    font-size: 34px;
    font-weight: 700;
    color: var(--ink-soft);
  }
  .card-front .person-name {
    position: absolute;
    left: 90px;
    top: 146px;
    font-size: 20px;
    font-weight: 700;
    color: var(--ink);
  }
  .card-front .name-rule {
    position: absolute;
    left: 90px;
    right: 40px;
    top: 178px;
    height: 1px;
    background: var(--ink-soft);
  }
  .contact-list {
    position: absolute;
    left: 90px;
    top: 190px;
    list-style: none;
  }
  .contact-list li {
    display: flex;
    align-items: center;
    gap: 10px;
    font-size: 14px;
    color: var(--ink-soft);
    line-height: 24px;
    white-space: nowrap;
  }
  .contact-list svg { width: 14px; height: 14px; fill: var(--ink); flex: none; }
  .card-front .address {
    position: absolute;
    left: 440px;
    top: 262px;
    font-size: 15px;
    line-height: 21px;
    color: var(--ink-soft);
  }
</style>
</head>
<body>

  <section class="card card-back" aria-label="Card back">
    <div class="brand"><span class="name">Kestrel Inquiries</span><span class="dot"></span></div>
    <div class="web"><span>kestrelinquiries-example.com.au</span><span class="rule"></span></div>
  </section>

  <section class="card card-front" aria-label="Card front">
    <div class="side-band"></div>
    <div class="brand"><span class="name">Kestrel Inquiries</span><span class="dot"></span></div>

    <p class="person-name">Morgan Pellwick</p>
    <div class="name-rule"></div>
    <ul class="contact-list">
      <li>
        <svg viewBox="0 0 16 16"><path d="M3 2h3l1.5 3.5-2 1.2a8 8 0 0 0 3.8 3.8l1.2-2L14 10v3a1 1 0 0 1-1 1C7 14 2 9 2 3a1 1 0 0 1 1-1z"/></svg>
        0487 362 914
      </li>
      <li>
        <svg viewBox="0 0 16 16"><path d="M1 3h14v10H1z M1 3l7 6 7-6" fill="none" stroke="#1b1b1d" stroke-width="1.6"/></svg>
        info@kestrelinquiries-example.com.au
      </li>
      <li>
        <svg viewBox="0 0 16 16"><circle cx="8" cy="8" r="7"/><path d="M1 8h14M8 1c-3 4-3 10 0 14M8 1c3 4 3 10 0 14" stroke="#fff" stroke-width="1" fill="none"/></svg>
        www.kestrelinquiries-example.com.au
      </li>
    </ul>

    <p class="address">PO Box 58<br>Ferndale NSW 2317</p>
  </section>

</body>
</html>
```